Rock, Paper Scissors Championship Flyer

We need a dynamic, bold and exciting flyer to promote the following event at our sports center. The event will be primarily focused for adults, but children are welcome to join

Rock, Paper, Scissors Championship - $$$ prizes
Date: June 9th, 2018
Time: 11am-4pm
Fee: $2 to enter, free for spectators
Heats to determine the overall ‘Rock, Paper, Scissors’ champion!
- Cash prizes on offer
- Live music.
- Food and beverage available for purchase

Belvorrow Sports Center, Hollin Falls
908-555-3162
www.belvorrowgrounds.example

Must include our logo (does not have to be huge) and County seal (both attached)

Colors

Designer to choose colors to be used in the design.

Requirements
Must have
• Should be fun and colorful
• The following info and attached logos:
• Rock, Paper, Scissors Championship - $$$ prizes
• Date: June 9th, 2018
• Time: 11am-4pm
• Fee: $2 to enter, free for spectators
• Heats to determine the overall ‘Rock, Paper, Scissors’ champion!
• - Cash prizes on offer
• - Live music.
• - Food and beverage available for purchase
• Belvorrow Sports Center, Hollin Falls
• 908-555-3162
• www.belvorrowgrounds.example
Nice to have
• There are a few inspirational photos attached to give an idea of what we are looking for.

```html
<!DOCTYPE html>
<html lang="en">
<head>
<meta charset="utf-8">
<title>Rock Paper Scissors Championship</title>
<link href="https://fonts.googleapis.com/css2?family=Oswald:wght@400;500;600&family=Open+Sans:wght@700&display=swap" rel="stylesheet">
<style>
  :root {
    --navy: #173e68;
    --navy-dark: #123357;
    --cream: #f7e9cf;
    --band: #f8ecd6;
    --ribbon-grey: #5c6670;
    --seal-gold: #d9b35a;
    --white: #ffffff;
  }
  html, body { margin: 0; padding: 0; overflow: hidden; }
  body { width: 833px; height: 1200px; }
  .flyer {
    position: relative;
    width: 833px;
    height: 1200px;
    overflow: hidden;
    background: linear-gradient(160deg, #34bfe6 0%, #5aa7df 22%, #8c6fbe 48%, #b56aaa 62%, #de5a92 80%, #ee7f85 100%);
    font-family: "Oswald", sans-serif;
  }
  .flyer__stripes { position: absolute; inset: 0; }
  .emblem { position: absolute; left: 0; top: 0; width: 833px; height: 720px; }
  .title-block {
    position: absolute; left: 0; width: 833px; top: 530px;
    text-align: center; color: var(--white);
  }
  .title-block__main {
    font-family: "Oswald", sans-serif; font-weight: 600;
    font-size: 58px; line-height: 1; letter-spacing: 0.5px; margin: 0;
  }
  .title-block__main .divider { font-weight: 400; margin: 0 10px; }
  .title-block__sub {
    font-family: "Open Sans", sans-serif; font-weight: 700;
    color: var(--cream); font-size: 31px; margin: 20px 0 0; line-height: 1;
  }
  .title-block__prizes {
    font-family: "Open Sans", sans-serif; font-weight: 700;
    color: var(--cream); font-size: 22px; margin: 8px 0 0; line-height: 1;
  }
  .details {
    position: absolute; left: 0; width: 833px; top: 726px;
    text-align: center; font-weight: 500; font-size: 32px; line-height: 50px;
  }
  .details p { margin: 0; }
  .details .label { color: var(--navy); }
  .details .value { color: var(--cream); }
  .details .gap { display: inline-block; width: 26px; }
  .highlights {
    position: absolute; left: 0; top: 842px; width: 833px; height: 78px;
    background: var(--band); color: var(--navy);
    font-size: 24px; font-weight: 500; line-height: 35px; text-align: center;
    padding-top: 4px; box-sizing: border-box;
  }
  .highlights p { margin: 0; white-space: nowrap; }
  .highlights .star { font-size: 13px; vertical-align: middle; margin: 0 6px 0 12px; }
  .brand {
    position: absolute; left: 60px; top: 1050px; width: 190px;
    display: flex; align-items: center; gap: 10px;
    color: var(--navy-dark); font-weight: 600; font-size: 24px; line-height: 1.1;
  }
  .brand__dot { width: 22px; height: 22px; border-radius: 50%; background: var(--navy-dark); flex: none; }
  .seal {
    position: absolute; left: 582px; top: 948px; width: 168px; height: 168px;
    border-radius: 50%; background: var(--seal-gold);
  }
  .footer {
    position: absolute; left: 0; top: 1128px; width: 833px; height: 44px;
    background: var(--navy); color: var(--white);
    font-size: 18px; font-weight: 500; line-height: 44px; white-space: nowrap;
  }
  .footer span { position: absolute; top: 0; }
  .footer__address { left: 48px; }
  .footer__phone { left: 372px; }
  .footer__web { right: 50px; }
</style>
</head>
<body>
<main class="flyer">
  <svg class="flyer__stripes" width="833" height="1200" viewBox="0 0 833 1200" aria-hidden="true">
    <g transform="rotate(-48 416 600)" opacity="0.35">
      <rect x="-200" y="80" width="1300" height="40" rx="20" fill="#7fe0ff"/>
      <rect x="-300" y="190" width="1200" height="24" rx="12" fill="#2d9fd6"/>
      <rect x="-100" y="300" width="1300" height="60" rx="30" fill="#9fe8ff"/>
      <rect x="-250" y="460" width="1200" height="30" rx="15" fill="#6a58a8"/>
      <rect x="-150" y="580" width="1300" height="50" rx="25" fill="#5fd0f0"/>
      <rect x="-200" y="740" width="1200" height="36" rx="18" fill="#c04c8f"/>
      <rect x="-100" y="860" width="1300" height="70" rx="35" fill="#f59a7a"/>
      <rect x="-300" y="1010" width="1300" height="28" rx="14" fill="#e8457f"/>
      <rect x="-100" y="1110" width="1200" height="50" rx="25" fill="#ffb48a"/>
    </g>
  </svg>

  <svg class="emblem" width="833" height="720" viewBox="0 0 833 720">
    <defs>
      <radialGradient id="emblem-bg" cx="50%" cy="45%" r="55%">
        <stop offset="0" stop-color="#f3f3f3"/>
        <stop offset="1" stop-color="#9aa3ac"/>
      </radialGradient>
      <linearGradient id="hands-fill" x1="0" y1="0" x2="0" y2="1">
        <stop offset="0" stop-color="#f6d3b4"/>
        <stop offset="1" stop-color="#eab894"/>
      </linearGradient>
    </defs>
    <circle cx="420" cy="342" r="282" fill="var(--navy)"/>
    <circle cx="420" cy="342" r="262" fill="url(#emblem-bg)"/>
    <rect x="208" y="92" width="432" height="390" rx="40" fill="url(#hands-fill)" opacity="0.85"
          role="img" aria-label="Illustration of three hands showing rock, paper and scissors"/>
    <polygon points="44,612 100,570 170,570 170,656 60,656 78,630" fill="var(--ribbon-grey)"/>
    <polygon points="789,612 733,570 663,570 663,656 773,656 755,630" fill="var(--ribbon-grey)"/>
    <polygon points="100,530 222,510 222,488 420,476 618,488 618,510 744,530 722,636 420,696 122,636"
             fill="var(--navy)"/>
    <line x1="140" y1="612" x2="270" y2="612" stroke="var(--cream)" stroke-width="1.5"/>
    <line x1="140" y1="618" x2="270" y2="618" stroke="var(--cream)" stroke-width="1.5"/>
    <line x1="140" y1="624" x2="270" y2="624" stroke="var(--cream)" stroke-width="1.5"/>
    <line x1="563" y1="612" x2="700" y2="612" stroke="var(--cream)" stroke-width="1.5"/>
    <line x1="563" y1="618" x2="700" y2="618" stroke="var(--cream)" stroke-width="1.5"/>
    <line x1="563" y1="624" x2="700" y2="624" stroke="var(--cream)" stroke-width="1.5"/>
  </svg>

  <header class="title-block">
    <h1 class="title-block__main">ROCK<span class="divider">|</span>PAPER<span class="divider">|</span>SCISSORS</h1>
    <p class="title-block__sub">CHAMPIONSHIP</p>
    <p class="title-block__prizes">$$$ PRIZES</p>
  </header>

  <section class="details">
    <p><span class="label">Date:</span> <span class="value">June 9th, 2018</span><span class="gap"></span><span class="label">Time:</span> <span class="value">11am-4pm</span></p>
    <p><span class="label">Fee:</span> <span class="value">$2 to enter, free for spectators</span></p>
  </section>

  <section class="highlights">
    <p><span class="star">★</span>Heats to determine the overall ‘Rock, Paper, Scissors’ champion!</p>
    <p><span class="star">★</span>Cash prizes on offer <span class="star">★</span>Live music <span class="star">★</span>Food and beverage available for purchase</p>
  </section>

  <div class="brand"><span class="brand__dot"></span><span>Belvorrow Sports Center</span></div>
  <div class="seal" role="img" aria-label="County seal"></div>

  <footer class="footer">
    <span class="footer__address">Belvorrow Sports Center, Hollin Falls</span>
    <span class="footer__phone">908-555-3162</span>
    <span class="footer__web">www.belvorrowgrounds.example</span>
  </footer>
</main>
</body>
</html>
```